Brimlock - a software development company requires letter head

I currently have a business card and logo, I just need a nice looking letter head the matches the two. I will upload these Illustrator files.

I would like the letter head to be done in a current version of MS Word.

Please incorporate 'brimlock' as per the attached font and the logo.

Industry/Entity Type

Computer Software

Colors

Designer to choose colors to be used in the design.

Requirements
Must have
• Fits in with current design, sleek and professional. It will be used for quotations and tenders and documentation going to clients and potential clients.
• Would like to company logo up the top header and perhaps a watermark of the logo at the bottom right, a bit like the business card.
• Also it needs to be MS word.
• Please work with the color pallet from the attached files.

```html
<!DOCTYPE html>
<html lang="en">
<head>
<meta charset="utf-8">
<title>Brimlock Letterhead</title>
<link rel="stylesheet" href="https://fonts.googleapis.com/css2?family=Open+Sans:wght@400;600&display=swap">
<style>
  :root {
    --backdrop: #ececec;
    --paper: #fcfcfc;
    --brand-blue: #29a3dc;
    --ink: #4a4a4a;
    --ink-soft: #5c5c5c;
    --watermark: #e2f0f8;
  }
  * { margin: 0; padding: 0; box-sizing: border-box; }
  html, body {
    width: 1200px;
    height: 1006px;
    overflow: hidden;
    background: var(--backdrop);
    font-family: "Open Sans", Arial, sans-serif;
  }
  .letterhead {
    position: absolute;
    left: 256px;
    top: 33px;
    width: 687px;
    height: 940px;
    background: var(--paper);
    overflow: hidden;
    box-shadow: 0 2px 6px rgba(0,0,0,0.15);
  }
  .brand {
    position: absolute;
    left: 78px;
    top: 92px;
    display: flex;
    align-items: center;
    gap: 10px;
  }
  .brand-dot {
    width: 22px;
    height: 22px;
    border-radius: 50%;
    background: var(--brand-blue);
  }
  .brand-name {
    font-size: 26px;
    font-weight: 600;
    letter-spacing: 1px;
    color: var(--ink);
  }
  .watermark {
    position: absolute;
    left: 360px;
    top: 660px;
    width: 440px;
    height: 440px;
    border-radius: 50%;
    background: var(--watermark);
  }
  .footer-tab {
    position: absolute;
    left: 0;
    top: 890px;
    width: 33px;
    height: 18px;
    background: var(--brand-blue);
    border-radius: 0 6px 6px 0;
  }
  .contact {
    position: absolute;
    left: 43px;
    top: 884px;
    font-size: 9.5px;
    line-height: 15px;
    color: var(--ink-soft);
  }
  .contact-line { display: flex; align-items: center; gap: 4px; white-space: nowrap; }
  .contact-line svg { width: 8px; height: 8px; fill: none; stroke: var(--brand-blue); stroke-width: 1.4; }
  .sep { margin: 0 3px; }
</style>
</head>
<body>
  <main class="letterhead">
    <header class="brand">
      <span class="brand-dot"></span>
      <span class="brand-name">BRIMLOCK</span>
    </header>

    <div class="watermark" aria-hidden="true"></div>

    <footer>
      <div class="footer-tab"></div>
      <address class="contact" style="font-style:normal">
        <div class="contact-line">41 Harbor Lane, Suite 12, Westbridge, CA 90412.</div>
        <div class="contact-line">
          <svg viewBox="0 0 10 10"><path d="M2 1 L4 1 L4.5 3 L3.3 4 Q4.5 6 6 6.7 L7 5.5 L9 6 L9 8 Q5 9 2 6 Q0.5 4 2 1Z"/></svg>
          <span>+1 555 014 7788</span><span class="sep">|</span>
          <svg viewBox="0 0 10 10"><rect x="1" y="2" width="8" height="6"/><path d="M1 2 L5 5.5 L9 2"/></svg>
          <span>hello@brimlock.dev</span><span class="sep">|</span>
          <svg viewBox="0 0 10 10"><circle cx="5" cy="5" r="4"/><path d="M1 5 H9 M5 1 Q2.5 5 5 9 M5 1 Q7.5 5 5 9"/></svg>
          <span>www.brimlock.dev</span>
        </div>
      </address>
    </footer>
  </main>
</body>
</html>
```